Water Remediation & Restoration Industry

Our company is in need of a trifold design for the water remediation & restoration industry. This brochure's main purpose is to help our company advertise its services to our community as well as insurance company's, home owners, and building managers. We currently run a commercial cleaning company and this is a new branch of service that we offer. We would like for the colors to coordinate with the logo which are royal blue, grey and white. We would like for the brochure to incorporate photos showing thermal imaging, equipment such as fans, dehumidifiers etc, water floods/leaks. We are a RTLVB Certified firm and the details to include are the following:
Phone Number: 1-866-307-5814
Website: www.pvdtservices.org
24 Hour Emergency Services
Emergency Mitigation
Water Extraction
Structural Drying
Dehumidication
Mold Remediation
Water Damage Restoration
Fire & Smoke Cleanup
Sewage & Toilet Overflows
Carpet & Upholstery Cleaning
Contents Cleaning
Monitoring/Coordination
Antimicrobial Application
Smoke & Odor Removal

```html
<!DOCTYPE html>
<html lang="en">
<head>
<meta charset="utf-8">
<title>PVDT Trifold Brochure</title>
<link href="https://fonts.googleapis.com/css2?family=Open+Sans:ital,wght@0,400;0,600;0,700;0,800;1,600&display=swap" rel="stylesheet">
<style>
  :root{
    --royal:#3a3187;
    --royal-deep:#2c2570;
    --grey:#8d8d92;
    --grey-light:#d6d6da;
    --white:#ffffff;
    --paper:#eeeef0;
    --ink:#2b2b33;
  }
  *{box-sizing:border-box;margin:0;padding:0}
  html,body{width:1200px;height:900px;overflow:hidden}
  body{background:var(--paper);font-family:"Open Sans",Arial,sans-serif;color:var(--ink);position:relative}
  .spread{position:absolute;left:45px;width:1110px;height:420px;background:var(--white);box-shadow:0 4px 16px rgba(0,0,0,.12);overflow:hidden}
  .spread-inside{top:22px}
  .spread-outside{top:458px}
  .spread-art{position:absolute;inset:0;width:1110px;height:420px}
  .fold{position:absolute;top:0;bottom:0;width:1px;background:rgba(0,0,0,.07)}
  .photo{position:absolute;border-radius:50%;border:8px solid var(--grey-light)}
  .heading{font-weight:800;text-transform:uppercase;letter-spacing:.3px;position:absolute}
  .on-blue{color:var(--white)}
  .on-white{color:var(--royal)}

  /* inside: about panel */
  .about-title{left:28px;top:26px;font-size:18px}
  .about-lead{position:absolute;left:28px;top:56px;width:300px;font-size:11.5px;font-weight:800;text-transform:uppercase;color:var(--white);line-height:1.25}
  .about-body{position:absolute;left:28px;top:90px;width:300px;font-size:10.5px;line-height:1.45;color:var(--white);text-align:justify}

  /* inside: quote badge */
  .quote-badge{position:absolute;left:500px;top:150px;width:118px;height:118px;border-radius:50%;background:var(--royal);border:6px solid var(--white);box-shadow:0 0 0 3px var(--grey-light);color:var(--white);text-align:center;padding-top:16px}
  .quote-badge svg{width:22px;height:22px}
  .quote-badge .quote-label{font-size:11px;font-weight:800;text-transform:uppercase;line-height:1.15;margin-top:2px}
  .quote-badge .quote-phone{font-size:10px;font-weight:700;margin-top:3px}

  .why-title{left:395px;top:282px;font-size:17px}
  .why-list{position:absolute;left:395px;top:312px;width:320px;list-style:none}
  .why-list li{position:relative;padding-left:24px;font-size:10.5px;font-style:italic;font-weight:600;color:var(--royal);line-height:1.3;margin-bottom:7px}
  .why-list li::before{content:"";position:absolute;left:0;top:1px;width:14px;height:14px;border:1.6px solid var(--royal);border-radius:50%}
  .why-list li::after{content:"";position:absolute;left:5px;top:4px;width:4px;height:7px;border:solid var(--royal);border-width:0 2px 2px 0;transform:rotate(45deg)}

  /* inside: services panel */
  .services-title{left:770px;top:22px;font-size:18px}
  .services-intro{position:absolute;left:770px;top:52px;width:310px;font-size:10.5px;line-height:1.45;color:var(--white);text-align:justify}
  .services-list{position:absolute;left:790px;top:160px;list-style:none}
  .services-list li{position:relative;padding-left:20px;font-size:11px;font-weight:600;color:var(--royal);line-height:17.2px}
  .services-list li::before{content:"";position:absolute;left:0;top:3px;width:12px;height:12px;border-radius:50%;background:var(--royal)}
  .services-list li::after{content:"";position:absolute;left:4px;top:5px;width:3px;height:6px;border:solid var(--white);border-width:0 1.6px 1.6px 0;transform:rotate(45deg)}

  /* outside: values panel */
  .values-title{left:30px;top:48px;font-size:18px}
  .values-list{position:absolute;left:30px;top:84px;list-style:none;color:var(--white)}
  .values-list li{font-size:14px;line-height:1.35}
  .values-list b{font-weight:800;display:inline-block;width:16px}
  .cert{position:absolute;left:70px;top:220px;width:110px;text-align:center}
  .cert-mark{width:46px;height:46px;border-radius:50%;background:var(--white);margin:0 auto 8px}
  .cert-label{font-size:13px;font-weight:800;color:var(--white);line-height:1.15;text-transform:uppercase}

  /* outside: contact */
  .contact-title{left:470px;top:262px;font-size:18px}
  .contact-list{position:absolute;left:470px;top:298px;list-style:none}
  .contact-list li{display:flex;align-items:center;gap:10px;font-size:11.5px;font-weight:600;color:var(--royal);margin-bottom:9px}
  .contact-list svg{width:16px;height:16px;flex:none}

  /* outside: cover */
  .cover-title{position:absolute;left:760px;top:18px;width:330px;text-align:center;font-size:18px;font-weight:800;text-transform:uppercase;color:var(--white);line-height:1.2}
  .brand{position:absolute;left:740px;top:296px;width:370px;display:flex;align-items:center;justify-content:center;gap:10px}
  .brand-mark{width:26px;height:26px;border-radius:50%;background:var(--royal)}
  .brand-name{font-size:30px;font-weight:800;color:var(--royal);letter-spacing:1px}
  .brand-sub{position:absolute;left:740px;top:334px;width:370px;text-align:center;font-size:10px;font-weight:600;color:var(--royal)}
  .cover-tagline{position:absolute;left:760px;top:366px;width:330px;text-align:center;font-size:12.5px;font-weight:600;color:var(--white);line-height:1.25}
</style>
</head>
<body>

<!-- Inside spread -->
<section class="spread spread-inside">
  <svg class="spread-art" viewBox="0 0 1110 420" aria-hidden="true">
    <path d="M0 0H370V205C270 255 120 255 0 225Z" fill="var(--royal)"/>
    <path d="M0 245C120 275 270 275 370 225" fill="none" stroke="var(--grey)" stroke-width="10"/>
    <path d="M370 420C420 380 520 385 600 420Z" fill="var(--royal)"/>
    <path d="M740 0H1110V115C1000 140 860 125 740 160Z" fill="var(--royal)"/>
    <path d="M740 175C860 140 1000 155 1110 130" fill="none" stroke="var(--grey)" stroke-width="9"/>
    <path d="M1110 330C1060 380 1000 405 930 420H1110Z" fill="var(--royal)"/>
    <path d="M880 420C980 400 1060 360 1110 310" fill="none" stroke="var(--grey)" stroke-width="8"/>
  </svg>
  <div class="fold" style="left:370px"></div>
  <div class="fold" style="left:740px"></div>

  <h2 class="heading on-blue about-title">About Us</h2>
  <p class="about-lead">Communication is the<br>key to our success.</p>
  <p class="about-body">Pine Valley Building Maintenance is committed to providing an unsurpassed level of janitorial services and building long-lasting relationships with clients. We accomplish this by using modern technology to communicate effectively with client's and employees.</p>
  <div class="photo" role="img" aria-label="Photo of a drying fan and dehumidifier in an empty room" style="left:70px;top:250px;width:165px;height:165px;background:linear-gradient(160deg,#e4e4e6,#9a9a9e)"></div>

  <div class="photo" role="img" aria-label="Photo of a worker handling water-damaged materials" style="left:445px;top:10px;width:150px;height:150px;background:linear-gradient(150deg,#d8d8da,#6f6f74)"></div>
  <div class="quote-badge">
    <svg viewBox="0 0 24 24"><path fill="#fff" d="M6.6 10.8a15 15 0 0 0 6.6 6.6l2.2-2.2c.3-.3.7-.4 1-.2 1.1.4 2.3.6 3.6.6.6 0 1 .4 1 1V20c0 .6-.4 1-1 1A17 17 0 0 1 3 4c0-.6.4-1 1-1h3.5c.6 0 1 .4 1 1 0 1.3.2 2.5.6 3.6.1.3 0 .7-.2 1Z"/></svg>
    <div class="quote-label">Request<br>Free Quote</div>
    <div class="quote-phone">1-866-307-5814</div>
  </div>
  <h2 class="heading on-white why-title">Why Choose Us</h2>
  <ul class="why-list">
    <li>We focus on our cleaners so that they can focus on you.</li>
    <li>We leverage technology to provide our clients clear &amp; consistent communication about the job we do.</li>
    <li>Quality is at the heart of why we do everything we do.</li>
  </ul>

  <h2 class="heading on-blue services-title">Our Services</h2>
  <p class="services-intro">When it comes to setting the standard of excellence in commercial cleaning, we will always be at the forefront of the industry. Our quality of service remains at the pinnacle of our mission.</p>
  <ul class="services-list">
    <li>24 Hour Emergency Services</li>
    <li>Emergency Mitigation</li>
    <li>Water Extraction</li>
    <li>Structural Drying</li>
    <li>Dehumidication</li>
    <li>Mold Remediation</li>
    <li>Water Damage Restoration</li>
    <li>Fire &amp; Smoke Cleanup</li>
    <li>Sewage &amp; Toilet Overflows</li>
    <li>Carpet &amp; Upholstery Cleaning</li>
    <li>Contents Cleaning</li>
    <li>Monitoring/Coordination</li>
    <li>Antimicrobial Application</li>
    <li>Smoke &amp; Odor Removal</li>
  </ul>
</section>

<!-- Outside spread -->
<section class="spread spread-outside">
  <svg class="spread-art" viewBox="0 0 1110 420" aria-hidden="true">
    <rect x="0" y="0" width="420" height="420" fill="var(--royal)"/>
    <path d="M350 0H740V420H380C450 380 460 300 420 235C380 170 330 90 350 0Z" fill="var(--white)"/>
    <path d="M380 420C450 380 460 300 420 235" fill="none" stroke="var(--grey)" stroke-width="9"/>
    <rect x="740" y="0" width="370" height="420" fill="var(--royal)"/>
    <path d="M740 260C850 320 1000 320 1110 250V365H740Z" fill="var(--white)"/>
    <path d="M740 262C850 322 1000 322 1110 252" fill="none" stroke="var(--grey)" stroke-width="9"/>
  </svg>
  <div class="fold" style="left:370px"></div>
  <div class="fold" style="left:740px"></div>

  <h2 class="heading on-blue values-title">Our Core Values</h2>
  <ul class="values-list">
    <li><b>P</b> – Patience</li>
    <li><b>V</b> – Vigilance</li>
    <li><b>D</b> – Dependability</li>
    <li><b>T</b> – Trust</li>
  </ul>
  <div class="cert">
    <div class="cert-mark"></div>
    <div class="cert-label">RTLVB<br>Certified</div>
  </div>

  <div class="photo" role="img" aria-label="Photo of a smiling customer service agent wearing a headset" style="left:290px;top:12px;width:190px;height:190px;background:linear-gradient(150deg,#e2e2e4,#7c7c80)"></div>
  <div class="photo" role="img" aria-label="Photo of a technician inspecting a leaking ceiling" style="left:265px;top:270px;width:140px;height:140px;background:linear-gradient(160deg,#c9b89a,#5d5a66)"></div>

  <h2 class="heading on-white contact-title">Contact Us</h2>
  <ul class="contact-list">
    <li><svg viewBox="0 0 24 24"><rect x="6" y="2" width="12" height="20" rx="2" fill="none" stroke="var(--royal)" stroke-width="1.8"/><circle cx="12" cy="18" r="1.2" fill="var(--royal)"/></svg>1-866-307-5814</li>
    <li><svg viewBox="0 0 24 24"><rect x="3" y="5" width="18" height="14" rx="1.5" fill="none" stroke="var(--royal)" stroke-width="1.8"/><path d="M3 6l9 7 9-7" fill="none" stroke="var(--royal)" stroke-width="1.8"/></svg>mreyes@pvdtservices.org</li>
    <li><svg viewBox="0 0 24 24"><circle cx="12" cy="12" r="9" fill="none" stroke="var(--royal)" stroke-width="1.8"/><path d="M3 12h18M12 3c3 3 3 15 0 18M12 3c-3 3-3 15 0 18" fill="none" stroke="var(--royal)" stroke-width="1.4"/></svg>www.pvdtservices.org</li>
  </ul>

  <h2 class="cover-title">Experience High-Tech<br>Efficiency</h2>
  <div role="img" aria-label="Photo of a homeowner catching ceiling leaks in blue buckets" style="position:absolute;left:760px;top:72px;width:330px;height:210px;border-radius:0 0 165px 165px / 0 0 70px 70px;background:linear-gradient(170deg,#c9c4d8,#6d6a8c 60%,#3b3a6e)"></div>
  <div class="brand">
    <span class="brand-mark"></span>
    <span class="brand-name">PVDT</span>
  </div>
  <p class="brand-sub">Commercial Cleaning &amp; Restoration</p>
  <p class="cover-tagline">Expertise &amp; experience<br>combined with advanced technology.</p>
</section>

</body>
</html>
```